Lumera Ostvik

I need you to design me a business card, with the same logo you did for my company.
It has to include this information.
Thx.
Contact details and other information I suppose it would be better if they were on the back of the card.
Company Name: LumeraOstvik
Commercial Name: Tomás Ibarra Quesada
Company activity: Cosmetics Distribution
Contact email: support@lumeost.com
Contact email: comercial@lumeost.com
Company website: https: //lumeost.com/
Company phone: +376 418 292
Instagram https://www.instagram.com/lumeraostvik/

```html
<!DOCTYPE html>
<html lang="en">
<head>
<meta charset="utf-8">
<title>Lumera Ostvik — Business Card</title>
<link href="https://fonts.googleapis.com/css2?family=Arimo:wght@400&family=Great+Vibes&display=swap" rel="stylesheet">
<style>
  :root {
    --backdrop: #e4e4e3;
    --card: #262626;
    --card-deep: #1f1f1f;
    --magenta: #c8159f;
    --ink-light: #e6e6e6;
    --rule: #bdbdbd;
    --emboss: #3a3a3a;
    --emboss-text: #5a5a5a;
  }
  * { box-sizing: border-box; margin: 0; padding: 0; }
  html, body { width: 1200px; height: 801px; overflow: hidden; }
  body {
    background: var(--backdrop);
    font-family: "Arimo", Arial, sans-serif;
    position: relative;
  }
  .card {
    position: absolute;
    top: 240px;
    width: 560px;
    height: 320px;
    background: var(--card);
    border-radius: 3px;
    box-shadow: 0 8px 22px rgba(0,0,0,.25);
  }
  .card-front { left: 25px; }
  .card-back { left: 615px; background: linear-gradient(135deg, var(--card) 0%, var(--card-deep) 100%); }

  .brand {
    position: absolute;
    left: 300px;
    top: 46px;
    display: flex;
    align-items: center;
    gap: 12px;
  }
  .brand-dot {
    width: 58px; height: 58px; border-radius: 50%;
    background: var(--magenta);
  }
  .brand-name {
    color: var(--magenta);
    font-size: 24px;
    letter-spacing: .5px;
  }

  .person {
    position: absolute;
    left: 34px;
    top: 150px;
  }
  .person-name {
    font-family: "Great Vibes", cursive;
    color: var(--magenta);
    font-size: 34px;
    line-height: 1;
  }
  .person-role {
    color: var(--ink-light);
    font-size: 15px;
    margin-top: 4px;
  }

  .divider {
    position: absolute;
    left: 34px; right: 30px;
    top: 222px;
    height: 1px;
    background: var(--rule);
  }

  .contacts {
    position: absolute;
    top: 236px;
    list-style: none;
    color: var(--ink-light);
    font-size: 14px;
  }
  .contacts-left { left: 34px; }
  .contacts-right { left: 330px; }
  .contacts li {
    display: flex; align-items: center; gap: 9px;
    height: 22px;
  }
  .contacts svg { width: 14px; height: 14px; fill: var(--magenta); flex: none; }

  .back-brand {
    position: absolute;
    left: 50%; top: 50%;
    transform: translate(-50%, -50%);
    display: flex;
    align-items: center;
    gap: 16px;
  }
  .back-dot {
    width: 120px; height: 120px; border-radius: 50%;
    background: var(--emboss);
    box-shadow: inset 2px 3px 6px rgba(0,0,0,.5);
  }
  .back-name {
    color: var(--emboss-text);
    font-size: 34px;
    letter-spacing: .5px;
  }
</style>
</head>
<body>
  <section class="card card-front">
    <div class="brand">
      <span class="brand-dot"></span>
      <span class="brand-name">Lumera Ostvik</span>
    </div>

    <div class="person">
      <p class="person-name">Tomás Ibarra Quesada</p>
      <p class="person-role">Cosmetics Distribution</p>
    </div>

    <div class="divider"></div>

    <ul class="contacts contacts-left">
      <li>
        <svg viewBox="0 0 16 16" aria-hidden="true"><path d="M3.6 1.2l2.3 2.6-1.3 1.7c.9 2 2.6 3.7 4.6 4.6l1.7-1.3 2.6 2.3-1.2 2.3C7.4 13.6 2.4 8.6 1.3 3.7z"/></svg>
        +376 418 292
      </li>
      <li>
        <svg viewBox="0 0 16 16" aria-hidden="true"><path d="M1 3h14v10H1zM2.5 4.5v.4L8 9l5.5-4.1v-.4z" fill-rule="evenodd"/></svg>
        support@lumeost.com
      </li>
      <li>
        <svg viewBox="0 0 16 16" aria-hidden="true"><path d="M1 3h14v10H1zM2.5 4.5v.4L8 9l5.5-4.1v-.4z" fill-rule="evenodd"/></svg>
        comercial@lumeost.com
      </li>
    </ul>

    <ul class="contacts contacts-right">
      <li>
        <svg viewBox="0 0 16 16" aria-hidden="true"><path d="M8 1a7 7 0 100 14A7 7 0 008 1zm0 1.6c.9 1 1.5 2.5 1.6 4.4H6.4C6.5 5.1 7.1 3.6 8 2.6zM6.4 8.6h3.2c-.1 1.9-.7 3.4-1.6 4.4-.9-1-1.5-2.5-1.6-4.4z"/></svg>
        www.lumeost.com
      </li>
      <li>
        <svg viewBox="0 0 16 16" aria-hidden="true"><rect x="2" y="2" width="12" height="12" rx="1"/></svg>
        lumeraostvik
      </li>
    </ul>
  </section>

  <section class="card card-back">
    <div class="back-brand">
      <span class="back-dot"></span>
      <span class="back-name">Lumera Ostvik</span>
    </div>
  </section>
</body>
</html>
```